Letterhead and business cards for criminal defense law firm
with existing logo
Letterhead and business cards for criminal defense law firm - Law
Creative Brief
Simple
The Law Office of Marcus Varek, PLLC
718 Birchwood Avenue, Suite 300 Houston, TX 77019
Varek@BrightCounselGroup.net
I would like to incorporate our slogan: Experienced criminal defense lawyers Or if you think of a better slogan/motto, feel free to incorporate it. I am not a flashy or showy lawyer. I want the card to invoke credibility, stability and intelligence (not an ambulance chaser or sleazy lawyer).

```html
<!DOCTYPE html>
<html lang="en">
<head>
<meta charset="utf-8">
<title>Marcus Varek — Business Card</title>
<link href="https://fonts.googleapis.com/css2?family=Montserrat:wght@600;700&family=Open+Sans:wght@400;600&display=swap" rel="stylesheet">
<style>
  :root {
    --navy: #1f2547;
    --navy-line: #4a5280;
    --grey-band: #5a5552;
    --paper: #ffffff;
    --ink: #3a3a3a;
    --ink-soft: #6b6b6b;
    --backdrop: #e4e5e7;
  }
  * { box-sizing: border-box; margin: 0; padding: 0; }
  html, body { width: 1200px; height: 901px; overflow: hidden; }
  body {
    background: var(--backdrop);
    font-family: "Open Sans", sans-serif;
    display: flex;
    align-items: center;
    justify-content: center;
    gap: 60px;
  }
  .card {
    width: 520px;
    height: 297px;
    position: relative;
    box-shadow: 0 6px 18px rgba(0,0,0,0.18);
  }

  /* Front */
  .card-front { background: var(--paper); }
  .front-band {
    position: absolute;
    left: 0; top: 44px;
    width: 112px; height: 26px;
    background: var(--grey-band);
  }
  .firm-mark {
    position: absolute;
    left: 122px; top: 38px;
    display: flex; align-items: center; gap: 10px;
  }
  .firm-mark .square {
    width: 38px; height: 38px; background: var(--navy);
  }
  .firm-name {
    font-family: "Montserrat", sans-serif;
    font-weight: 700;
    color: var(--navy);
    font-size: 15px;
    line-height: 1.15;
    text-transform: uppercase;
    letter-spacing: 0.5px;
    max-width: 250px;
  }
  .person {
    position: absolute;
    right: 36px; top: 104px;
    text-align: right;
  }
  .person-name { font-size: 15px; color: var(--ink); }
  .person-title { font-size: 8px; color: var(--ink-soft); margin-top: 2px; }
  .contact {
    position: absolute;
    left: 26px; top: 160px;
    font-size: 9.5px;
    color: var(--ink);
    line-height: 1.45;
  }
  .contact .address { margin-bottom: 10px; }
  .contact-row { display: flex; align-items: center; gap: 6px; }
  .contact-row svg { width: 9px; height: 9px; fill: var(--navy); flex: none; }

  /* Back */
  .card-back { background: var(--navy); }
  .back-frame {
    position: absolute; inset: 12px;
    border: 1px solid var(--navy-line);
  }
  .back-mark {
    position: absolute; inset: 0;
    display: flex; align-items: center; justify-content: center; gap: 12px;
  }
  .back-mark .square {
    width: 44px; height: 44px; background: var(--paper);
  }
  .back-mark .firm-name { color: var(--paper); font-size: 17px; max-width: 290px; }
</style>
</head>
<body>
  <section class="card card-back">
    <div class="back-frame"></div>
    <div class="back-mark">
      <div class="square"></div>
      <div class="firm-name">The Law Office of Marcus Varek, PLLC</div>
    </div>
  </section>

  <section class="card card-front">
    <div class="front-band"></div>
    <div class="firm-mark">
      <div class="square"></div>
      <div class="firm-name">The Law Office of Marcus Varek, PLLC</div>
    </div>
    <div class="person">
      <div class="person-name">Marcus Varek</div>
      <div class="person-title">Attorney at Law</div>
    </div>
    <div class="contact">
      <div class="address">718 Birchwood Avenue, Suite 300<br>Houston, TX 77019</div>
      <div class="contact-row">
        <svg viewBox="0 0 10 10"><path d="M2 0h2l1 3-1.5 1a6 6 0 0 0 2.5 2.5L7 5l3 1v2a2 2 0 0 1-2 2A8 8 0 0 1 0 2a2 2 0 0 1 2-2z"/></svg>
        <span>713-555-0142</span>
      </div>
      <div class="contact-row">
        <svg viewBox="0 0 10 10"><rect x="2.5" y="0" width="5" height="10" rx="1"/></svg>
        <span>713-555-0187</span>
      </div>
      <div class="contact-row">
        <svg viewBox="0 0 10 10"><rect x="0" y="3" width="10" height="5"/><rect x="2" y="0" width="6" height="3"/></svg>
        <span>713-555-0163</span>
      </div>
      <div class="contact-row">
        <svg viewBox="0 0 10 10"><path d="M0 2h10v6H0z"/></svg>
        <span>Varek@BrightCounselGroup.net</span>
      </div>
    </div>
  </section>
</body>
</html>
```